Valtrix Inc

Hello.

I would like to take a wordpress ecomm template and turn it into a website that can display 100s of domain listings with short text box for description and a price .
One link to quibblepay.example for immediate payment and with the confirmation/decline letter/email .
Five - six pages, Home, about us, domains, contact us, . Several columns or scrolling page for the domain page. I want to list several hundred virtual domains for sale .
Like a portfolio website but lists domain text .
This will be hosted on my server. On my domain.

Target Market(s)

End users, business owners, store front managers, online entpenauers , ect

Industry/Entity Type

Information Technology

Number of Pages Required

5+ page

Font styles to use
Sans Serif

Colors
0455a3
f78f20
abd036

Requirements
Must have
• Lots of white space, clean professional look . fast loading , use of greens and blues. Easy to read font.
• big headers , several - three different headers that rotate or move or clicks.
• A few current stock photos.
Should not have
• slow loading photos.
• More than two photos on any one page.

```html
<!DOCTYPE html>
<html lang="en">
<head>
<meta charset="utf-8">
<title>Brightpath Domains</title>
<link href="https://fonts.googleapis.com/css2?family=Montserrat:wght@400;600;700;800&family=Open+Sans:wght@400;600;700&display=swap" rel="stylesheet">
<style>
:root{
  --blue:#0455a3;
  --blue-dark:#034382;
  --green:#abd036;
  --orange:#f78f20;
  --ink:#222831;
  --muted:#6b7280;
  --line:#dfe3e8;
  --tile:#f1f2f4;
  --footer:#2d4763;
  --footer-deep:#243a52;
  --white:#ffffff;
}
*{margin:0;padding:0;box-sizing:border-box}
html,body{width:1200px;height:2288px;overflow:hidden}
body{font-family:"Open Sans",Arial,sans-serif;color:var(--ink);background:var(--white);position:relative}
.heading{font-family:"Montserrat",Arial,sans-serif}

/* header */
.site-header{position:absolute;top:0;left:0;width:1200px;height:56px;background:var(--white);display:flex;align-items:center;padding:0 80px;justify-content:space-between;box-shadow:0 1px 3px rgba(0,0,0,.08);z-index:2}
.brand{font-family:"Montserrat",Arial,sans-serif;font-weight:700;font-size:22px;color:var(--blue);letter-spacing:.5px;display:flex;align-items:center;gap:8px}
.brand-dot{width:10px;height:10px;background:var(--green)}
.main-nav{display:flex;align-items:center;gap:22px;font-size:12px;font-weight:600;color:var(--ink)}
.main-nav .btn{padding:7px 14px;color:var(--white);font-size:11px;border-radius:2px}
.btn-login{background:var(--blue)}
.btn-register{background:var(--green)}

/* hero */
.hero{position:absolute;top:56px;left:0;width:1200px;height:524px;overflow:hidden;
  background:linear-gradient(90deg,#f4f5f4 0%,#eceeec 45%,#d9ddd8 70%,#c9cfc8 100%)}
.hero-photo{position:absolute;right:0;top:0;width:620px;height:524px;
  background:linear-gradient(100deg,rgba(240,242,240,0) 0%,rgba(205,210,204,.7) 40%,rgba(160,170,165,.6) 100%)}
.hero-copy{position:absolute;left:0;right:0;top:244px;text-align:center}
.hero-title{font-family:"Montserrat",Arial,sans-serif;font-weight:800;font-size:54px;color:#1b1e22;letter-spacing:-.5px}
.hero-sub{font-family:"Montserrat",Arial,sans-serif;font-weight:400;font-size:34px;color:#2b2f33;margin-top:2px}

/* search band */
.search-band{position:absolute;top:580px;left:0;width:1200px;height:80px;background:var(--blue);display:flex;align-items:center;padding:0 80px;gap:60px}
.search-intro h2{font-family:"Montserrat",Arial,sans-serif;font-size:26px;font-weight:700;color:var(--white)}
.search-intro p{font-size:13px;color:#d6e4f3;margin-top:2px}
.search-form{display:flex;gap:12px}
.search-input{width:330px;height:34px;background:var(--white);border-radius:2px;font-size:11px;color:#8a8f96;display:flex;align-items:center;padding:0 12px}
.search-select{width:150px;height:34px;background:var(--white);border-radius:2px;font-size:11px;color:#8a8f96;display:flex;align-items:center;justify-content:space-between;padding:0 12px}
.search-btn{width:130px;height:34px;background:var(--green);color:var(--white);font-size:12px;font-weight:700;display:flex;align-items:center;justify-content:center;border-radius:2px}

/* domain listings */
.domains{position:absolute;top:660px;left:0;width:1200px;height:780px;background:var(--white)}
.domain-board{position:absolute;top:40px;left:132px;width:936px;height:620px;border:1px solid var(--line);background:var(--white)}
.section-title{font-family:"Montserrat",Arial,sans-serif;font-weight:700;font-size:38px;text-align:center;color:var(--ink)}
.section-title .accent{color:var(--green)}
.domain-board .section-title{margin-top:34px}
.title-rule{width:640px;height:1px;background:var(--line);margin:18px auto 0}
.domain-grid{display:grid;grid-template-columns:repeat(4,180px);column-gap:60px;row-gap:22px;justify-content:center;margin-top:34px}
.domain-tile{height:38px;background:var(--tile);border:1px solid #e6e8eb;font-size:11px;font-weight:600;color:#3b4046;display:flex;align-items:center;justify-content:center;letter-spacing:.3px}
.domain-tile.is-active{border:2px solid var(--blue);background:#e9f1fa;color:var(--blue);position:relative}
.view-all{position:absolute;top:692px;left:540px;width:120px;height:30px;background:var(--green);color:var(--white);font-size:11px;font-weight:700;display:flex;align-items:center;justify-content:center;border-radius:2px}

/* welcome */
.welcome{position:absolute;top:1440px;left:0;width:1200px;height:200px;overflow:hidden;
  background:linear-gradient(180deg,#e4ebf2 0%,#d6e0ea 60%,#e9eef3 100%)}
.welcome-photo{position:absolute;inset:0;background:linear-gradient(90deg,rgba(120,150,180,.35) 0%,rgba(255,255,255,.1) 45%,rgba(150,175,200,.45) 100%)}
.welcome-copy{position:absolute;left:150px;right:150px;top:50px;text-align:center}
.welcome-copy p{font-size:12px;line-height:18px;color:#3a4048;margin-top:14px}

/* testimonials */
.testimonials{position:absolute;top:1640px;left:0;width:1200px;height:348px;background:#eceef0}
.testimonials .section-title{margin-top:62px}
.quote{position:absolute;top:140px;left:200px;width:800px;text-align:center;font-size:12px;line-height:18px;color:#4a5058}
.quote-mark{position:absolute;top:136px;left:168px;font-family:"Montserrat",Arial,sans-serif;font-size:44px;line-height:40px;color:#9aa3ad}
.avatars{position:absolute;top:222px;left:0;width:1200px;display:flex;justify-content:center;gap:26px;align-items:center}
.avatar{width:56px;height:56px;border-radius:50%;background:#c9cfd6;border:3px solid var(--white);box-shadow:0 1px 3px rgba(0,0,0,.2)}
.avatar.is-current{width:74px;height:74px;background:#b7c4d2;border-color:var(--green)}
.reviewer{position:absolute;top:310px;left:0;width:1200px;text-align:center;font-size:11px;font-weight:700;color:#3a4048}

/* footer */
.site-footer{position:absolute;top:1988px;left:0;width:1200px;height:300px;background:var(--footer);color:var(--white)}
.contact-row{position:absolute;top:30px;left:140px;width:920px;display:flex;align-items:center;justify-content:space-between}
.contact-item{display:flex;align-items:center;gap:12px}
.contact-icon{width:36px;height:36px;border-radius:50%;background:var(--green);display:flex;align-items:center;justify-content:center}
.contact-item h4{font-size:12px;font-weight:700}
.contact-item p{font-size:11px;color:#c7d3df}
.social-box{border:1px solid #5c7590;padding:10px 16px;display:flex;gap:8px}
.social-box span{width:22px;height:22px;background:#4f6a86;border-radius:2px}
.footer-nav{position:absolute;top:142px;left:0;width:1200px;display:flex;justify-content:center;gap:70px;font-size:11px;font-weight:600;color:#dbe4ec}
.footer-rule{position:absolute;top:126px;left:140px;width:920px;height:1px;background:#44607d}
.copyright{position:absolute;top:176px;left:0;width:1200px;text-align:center;font-size:10px;color:#aebccb}
.footer-base{position:absolute;bottom:0;left:0;width:1200px;height:84px;background:var(--footer-deep)}
</style>
</head>
<body>

<header class="site-header">
  <div class="brand"><span class="brand-dot"></span>BRIGHTPATH DOMAINS</div>
  <nav class="main-nav">
    <span>HOME</span><span>ABOUT US</span><span>DOMAINS</span><span>CONTACT US</span>
    <span class="btn btn-login">LOGIN</span>
    <span class="btn btn-register">REGISTER</span>
  </nav>
</header>

<section class="hero">
  <div class="hero-photo" role="img" aria-label="Stock photo of a smiling man in a shirt using a tablet in a bright office"></div>
  <div class="hero-copy">
    <h1 class="hero-title">THE BEST DOMAINS FOR</h1>
    <p class="hero-sub">The Brightest Of Ideas</p>
  </div>
</section>

<section class="search-band">
  <div class="search-intro">
    <h2>Looking For a Domain?</h2>
    <p>Follow the simple steps below to find yours now!</p>
  </div>
  <div class="search-form">
    <div class="search-input">Enter Domain To Search</div>
    <div class="search-select">.com
      <svg width="10" height="6" viewBox="0 0 10 6"><path d="M0 0l5 6 5-6z" fill="#8a8f96"/></svg>
    </div>
    <div class="search-btn">SEARCH</div>
  </div>
</section>

<section class="domains">
  <div class="domain-board">
    <h2 class="section-title">Find Your <span class="accent">Domain</span></h2>
    <div class="title-rule"></div>
    <div class="domain-grid">
      <div class="domain-tile">LOREM-IPSUM.COM</div><div class="domain-tile">LOREM-IPSUM.COM</div><div class="domain-tile">LOREM-IPSUM.COM</div><div class="domain-tile">LOREM-IPSUM.COM</div>
      <div class="domain-tile">MAGNA-ALIQUAM.COM</div><div class="domain-tile">NIMMY-VENIAM.COM</div><div class="domain-tile">MAGNA-ALIQUAM.COM</div><div class="domain-tile">NIMMY-VENIAM.COM</div>
      <div class="domain-tile is-active">CONSECTETUER.COM</div><div class="domain-tile">CODO-CONSEQUA.COM</div><div class="domain-tile">CONSECTETUER.COM</div><div class="domain-tile">CODO-CONSEQUA.COM</div>
      <div class="domain-tile">NIMMY-VENIAM.COM</div><div class="domain-tile">CONSECTETUER.COM</div><div class="domain-tile">NIMMY-VENIAM.COM</div><div class="domain-tile">CONSECTETUER.COM</div>
      <div class="domain-tile">CODO-CONSEQUA.COM</div><div class="domain-tile">NIMMY-VENIAM.COM</div><div class="domain-tile">CODO-CONSEQUA.COM</div><div class="domain-tile">NIMMY-VENIAM.COM</div>
      <div class="domain-tile">CONSECTETUER.COM</div><div class="domain-tile">CODO-CONSEQUA.COM</div><div class="domain-tile">CONSECTETUER.COM</div><div class="domain-tile">CODO-CONSEQUA.COM</div>
      <div class="domain-tile">LOREM-IPSUM.COM</div><div class="domain-tile">MAGNA-ALIQUAM.COM</div><div class="domain-tile">LOREM-IPSUM.COM</div><div class="domain-tile">MAGNA-ALIQUAM.COM</div>
    </div>
  </div>
  <div class="view-all">VIEW ALL</div>
</section>

<section class="welcome">
  <div class="welcome-photo" role="img" aria-label="Faded stock photo of a city skyline seen from a high office window"></div>
  <div class="welcome-copy">
    <h2 class="section-title">Welcome To <span class="accent">Brightpath Domains</span></h2>
    <p>Browse hundreds of hand picked names ready for your next venture. Every listing shows a short note and a clear price, and checkout takes a single step through our secure payment partner. Once paid, you receive a confirmation email with transfer details, and our team stays with you until the name is live on your own server.</p>
  </div>
</section>

<section class="testimonials">
  <h2 class="section-title">People <span class="accent">Love Us!</span></h2>
  <span class="quote-mark">&ldquo;</span>
  <p class="quote">I found the perfect name for my shop in minutes. The listings were easy to scan, the price was fair, and payment went through right away. The transfer was done the same day and support answered every question I had.</p>
  <div class="avatars">
    <div class="avatar" role="img" aria-label="Customer portrait"></div>
    <div class="avatar is-current" role="img" aria-label="Portrait of the quoted customer"></div>
    <div class="avatar" role="img" aria-label="Customer portrait"></div>
  </div>
  <p class="reviewer">MR. Lorem Ipsum</p>
</section>

<footer class="site-footer">
  <div class="contact-row">
    <div class="contact-item">
      <span class="contact-icon"><svg width="16" height="18" viewBox="0 0 16 18"><path d="M8 0a6 6 0 0 0-6 6c0 4.5 6 12 6 12s6-7.5 6-12a6 6 0 0 0-6-6zm0 8.5A2.5 2.5 0 1 1 8 3.5a2.5 2.5 0 0 1 0 5z" fill="#fff"/></svg></span>
      <div><h4>BRIGHTPATH DOMAINS</h4><p>120 Harbor Lane, Suite 4, Springfield</p></div>
    </div>
    <div class="contact-item">
      <span class="contact-icon"><svg width="16" height="16" viewBox="0 0 16 16"><path d="M3.2 1l2.6 3.2-1.4 1.8a9 9 0 0 0 5.6 5.6l1.8-1.4L15 12.8 13.4 15C6.8 15 1 9.2 1 2.6z" fill="#fff"/></svg></span>
      <div><h4>CALL US :</h4><p>+1 (555) 014-2290</p></div>
    </div>
    <div class="contact-item">
      <span class="contact-icon"><svg width="18" height="12" viewBox="0 0 18 12"><rect x="0.5" y="0.5" width="17" height="11" fill="none" stroke="#fff"/><path d="M1 1l8 6 8-6" fill="none" stroke="#fff"/></svg></span>
      <div><h4>EMAIL US :</h4><p>hello@brightpath.example</p></div>
    </div>
    <div class="social-box"><span></span><span></span><span></span><span></span></div>
  </div>
  <div class="footer-rule"></div>
  <div class="footer-base"></div>
  <nav class="footer-nav"><span>HOME</span><span>ABOUT US</span><span>DOMAINS</span><span>CONTACT US</span></nav>
  <p class="copyright">Copyright &copy; 2024 Brightpath Domains. All Rights Reserved.</p>
</footer>

</body>
</html>
```